Banner for promote service of debit card

We are PagaVelo and we need the banners to be posted on the facebook and instagram pages.
We want something to communicate that it is an exclusive debit card full of services.
Low commissions.
Our competitors:
https://www.nortapay-pagos.it/it/home.html
https://www.zelkor-conti.it/it/
https://www.fotoreelz.it/serravanbank/
sendquillo
maybe some banner that makes the idea of a convenient debit card that everyone can use.
Girls enjoying card shopping.
Please check also website for slogans and phrases to use
https://www.pagavelo-carta.it/
Should show the services.
We must convey that it is a fast, simple card that guarantees privacy.
We need strong banners that attract people as these ban will be sponsored on instagram and facebook
Target Market(s)
People 18-35 y
Open Bank account. low commissions. Easy to use. No limits. 100% Privacy.
Requirements
Must have
- Written in Italian.

```html
<!DOCTYPE html>
<html lang="it">
<head>
<meta charset="UTF-8">
<title>PagaVelo – Alimenta il tuo potenziale</title>
<link rel="stylesheet" href="https://fonts.googleapis.com/css2?family=Open+Sans:wght@600;700&family=Varela+Round&display=swap">
<style>
  :root {
    --bg-top: #8fdde3;
    --bg-bottom: #5fc5cf;
    --bg-soft: #b9ecef;
    --purple: #a1119c;
    --purple-dark: #7f0b86;
    --white: #ffffff;
    --photo-a: #c9a088;
    --photo-b: #a8174f;
    --logo-text: #8a7fa8;
  }
  * { margin: 0; padding: 0; box-sizing: border-box; }
  html, body { width: 1200px; height: 1200px; overflow: hidden; }
  body { background: var(--bg-bottom); }
  .canvas {
    position: relative;
    width: 1200px;
    height: 1200px;
    overflow: hidden;
    background: linear-gradient(160deg, var(--bg-top) 0%, var(--bg-soft) 45%, var(--bg-bottom) 100%);
    font-family: "Open Sans", sans-serif;
  }
  .decor { position: absolute; inset: 0; width: 1200px; height: 1200px; }
  .headline-band {
    position: absolute;
    left: 125px; top: 78px;
    width: 1005px; height: 102px;
    background: var(--purple);
    border-radius: 0 8px 8px 0;
    display: flex; align-items: center; justify-content: center;
  }
  .headline-band h1 {
    color: var(--white);
    font-weight: 700;
    font-size: 64px;
    letter-spacing: 0.5px;
  }
  .hero-photo {
    position: absolute;
    left: 90px; top: 200px;
    width: 680px; height: 1000px;
    border-radius: 300px 300px 0 0;
    background: linear-gradient(180deg, var(--photo-a) 0%, #b56a6a 40%, var(--photo-b) 70%, #8d1248 100%);
    opacity: 0.85;
  }
  .benefits { position: absolute; inset: 0; list-style: none; }
  .benefit {
    position: absolute;
    background: var(--purple);
    color: var(--white);
    font-family: "Varela Round", sans-serif;
    font-size: 41px;
    line-height: 1;
    padding: 14px 26px 16px;
    border-radius: 10px;
    transform: rotate(-3deg);
    white-space: nowrap;
  }
  .benefit--1 { left: 770px; top: 290px; }
  .benefit--2 { left: 715px; top: 385px; }
  .benefit--3 { left: 830px; top: 487px; }
  .benefit--4 { left: 750px; top: 588px; }
  .brand {
    position: absolute;
    right: 40px; bottom: 36px;
    display: flex; align-items: center; gap: 14px;
  }
  .brand-dot {
    width: 30px; height: 30px;
    border-radius: 50%;
    background: var(--purple);
  }
  .brand-name {
    color: var(--logo-text);
    font-weight: 700;
    font-size: 34px;
  }
</style>
</head>
<body>
  <main class="canvas">
    <svg class="decor" viewBox="0 0 1200 1200" aria-hidden="true">
      <line x1="-60" y1="520" x2="330" y2="260" stroke="#c2eef2" stroke-width="130" stroke-linecap="round"/>
      <line x1="60" y1="520" x2="250" y2="390" stroke="var(--purple)" stroke-width="30" stroke-linecap="round"/>
      <line x1="20" y1="600" x2="110" y2="545" stroke="#c8f0f3" stroke-width="40" stroke-linecap="round"/>
      <circle cx="80" cy="420" r="24" fill="none" stroke="#ffffff" stroke-width="6"/>
      <circle cx="630" cy="470" r="18" fill="none" stroke="#ffffff" stroke-width="5"/>
      <line x1="420" y1="1060" x2="780" y2="700" stroke="#bfeef2" stroke-width="110" stroke-linecap="round"/>
      <line x1="920" y1="610" x2="1180" y2="280" stroke="#c9f1f4" stroke-width="70" stroke-linecap="round"/>
      <line x1="1000" y1="930" x2="1160" y2="780" stroke="#ffffff" stroke-width="3"/>
      <path d="M1020 1200 C1060 1000 1200 960 1200 960 L1200 1200 Z" fill="#4fb4c2"/>
      <circle cx="940" cy="1120" r="22" fill="none" stroke="#ffffff" stroke-width="5"/>
      <line x1="-20" y1="1150" x2="200" y2="920" stroke="#ffffff" stroke-width="55" stroke-linecap="round"/>
    </svg>

    <div class="hero-photo" role="img" aria-label="Foto di una ragazza sorridente con occhiali e maglione fucsia che tiene uno smartphone e fa il segno OK"></div>

    <svg class="decor" viewBox="0 0 1200 1200" aria-hidden="true">
      <line x1="420" y1="1040" x2="760" y2="700" stroke="var(--purple)" stroke-width="30" stroke-linecap="round"/>
    </svg>

    <header class="headline-band">
      <h1>Alimenta il tuo potenziale</h1>
    </header>

    <ul class="benefits">
      <li class="benefit benefit--1">Enjoy you cart</li>
      <li class="benefit benefit--2">Fai quello Che vuoi</li>
      <li class="benefit benefit--3">Nessun limite</li>
      <li class="benefit benefit--4">Nessun controllo</li>
    </ul>

    <footer class="brand">
      <span class="brand-dot"></span>
      <span class="brand-name">PagaVelo</span>
    </footer>
  </main>
</body>
</html>
```